Innovative label design for premium vodka bottle

We are looking for a bottle design (with logo) for a new premium vodka company based in Uganda. We are the first company to produce a premium vodka in Uganda made exclusively with local ingredients. We want the label design to set us apart from the more traditional (read boring) designs of local packaging and bring raise the bar for Ugandan packaging design.

We will initially sell to local markets and hope to go global in two years. The vodka is called "IRONCREST" after the famous adult mountain gorillas which live in the mountains of western Uganda.

The bottle design has to be simple and appealing to both an Africana and an International consumer (tourists). Simple, clean and to the point. The main color should be green and can or cannot include a rendering of a gorilla. Silver must also be included in the design (could be printed on metallic paper). It also can include the mountain landscapes of western Uganda. But please we are also open to more creative ideas which stray from these typical images of Uganda. I will attach some images of the silverback, the mountains of Uganda and other labels of local alcoholic beverages. Must be printed on paper. Can be glossy, matte or metallic. Do not submit ideas for labels printing on transparent film.

The size of the label should be 75mm wide by 120mm high. Also attached is an image of the bottle to be used.

Text that MUST be on the label:

Ironcrest
Ultra-Premium Vodka
Produced in Uganda
Triple Distilled from Sugar Cane
42.5%ABV
700ML

Text that CAN be incorporated:
Purely Ugandan
Triple Distilled-Ten Times filtered
3X Distilled - 10X Filtered

Please feel free to contact me with any inquiries.
Updates

Project Deadline Extended
Reason: Since we cannot meet until Wednesday to consider the designs, may as well allow the crowd a couple more days of creativity. Cheers, Bram

Hi,

Thank you all for your updates. We are currently ging through the designs and hope to have a decision made by the end of the week.

Well done!

Cheers,

Bram

Target Market(s)

Upmarket Ugandans and International consumers

Industry/Entity Type

Adult

Requirements
Must have
• Must be printed on paper. Can be glossy, matte or metallic. Do not submit ideas for labels printing on transparent film.

```html
<!DOCTYPE html>
<html lang="en">
<head>
<meta charset="utf-8">
<title>Ironcrest Vodka Label</title>
<link rel="stylesheet" href="https://fonts.googleapis.com/css2?family=Oswald:wght@700&family=Cinzel:wght@400;600&display=swap">
<style>
  :root {
    --backdrop: #eef0ef;
    --label-white: #ffffff;
    --label-mist: #c9cbc9;
    --label-slate: #5b605b;
    --label-deep: #2a2f2a;
    --label-black: #0b130b;
    --wordmark: #14301a;
    --silver-text: #b9bdb9;
    --region-light: #6f756f;
    --region-dark: #3a423a;
  }
  * { margin: 0; padding: 0; box-sizing: border-box; }
  html, body {
    width: 1200px;
    height: 2863px;
    overflow: hidden;
    background: var(--backdrop);
  }
  .label {
    position: absolute;
    left: 100px;
    top: 651px;
    width: 1000px;
    height: 1560px;
    background: linear-gradient(to bottom,
      var(--label-white) 0px,
      var(--label-white) 180px,
      var(--label-mist) 300px,
      var(--label-slate) 520px,
      var(--label-deep) 900px,
      var(--label-black) 1560px);
    overflow: hidden;
  }
  .wordmark {
    position: absolute;
    left: 0;
    width: 100%;
    top: 215px;
    text-align: center;
    font-family: "Oswald", sans-serif;
    font-weight: 700;
    font-size: 196px;
    line-height: 1;
    letter-spacing: 2px;
    color: var(--wordmark);
  }
  .tagline {
    position: absolute;
    left: 0;
    width: 100%;
    top: 462px;
    text-align: center;
    font-family: "Cinzel", serif;
    font-weight: 600;
    font-size: 40px;
    letter-spacing: 2px;
    color: var(--silver-text);
  }
  .region-map {
    position: absolute;
    left: 165px;
    top: 540px;
    width: 640px;
    height: 840px;
    border-radius: 40% 30% 35% 45%;
    background: radial-gradient(ellipse at 50% 40%, var(--region-light), var(--region-dark) 75%, transparent 100%);
    opacity: 0.55;
  }
  .process {
    position: absolute;
    left: 0;
    width: 100%;
    top: 1388px;
    text-align: center;
    font-family: "Cinzel", serif;
    font-weight: 600;
    color: var(--silver-text);
    line-height: 1.15;
  }
  .process .distilled { font-size: 34px; letter-spacing: 1px; }
  .process .filtered { font-size: 34px; letter-spacing: 2px; }
  .spec {
    position: absolute;
    top: 1506px;
    font-family: "Cinzel", serif;
    font-weight: 400;
    font-size: 28px;
    color: var(--region-light);
  }
  .spec-abv { left: 20px; }
  .spec-volume { right: 24px; }
</style>
</head>
<body>
  <main class="label">
    <h1 class="wordmark">IRONCREST</h1>
    <p class="tagline">Purely Ugadan Ultra Premium Vodka</p>
    <div class="region-map" role="img" aria-label="Outline map of Uganda"></div>
    <div class="process">
      <p class="distilled">Triple Distilled From Sugar Cane</p>
      <p class="filtered">10X FILTERED</p>
    </div>
    <p class="spec spec-abv">42.5% ABV</p>
    <p class="spec spec-volume">700 ML</p>
  </main>
</body>
</html>
```